Increased budget: GUI redesign: 10 year old user interface needs modern look-and-feel

UPDATE: Please DO look at more than only th eone image I attached! Almost all designs are simply reworks of that one picture. That is not what we are looking for. Check out the video to understand what the product does, and try to make something better.
We have an existing app (see https://www.vextorane.com/downloadBrivoPanel.php?vers=3_9_1_140964&dir=Vextorane_OEM/3_9_1_140964&name=DSP_Control_Software) which needs refreshing. See also a video here: https://vextorane-oem.com/software/ and the user manual attached here. The GUI is now 800x400 pixels, which is too small; and not scalable, which will be fixed in the future. We need a new, modern look-and-feel, and images that can be exported from the design in various sizes. The current design is attached as well as a collection of PNG files. The overall layout can stay similar, although we are open to good ideas for improvements. The design should be targeted at professional users, not end users; the product is used by audio professionals (e.g. sound engineers, loudspeaker designers). Also see our web version: https://www.vextorane.com/brivopanel/skins/1_1_2/container.html?MAC=Demo%201x2
The winner will also be asked to do a full design of the application GUI (based on the design done here), with several more windows etc, and additional payment depending on the work to be done.

Target Market(s)

Professional audio

Industry/Entity Type

Audio / Industrial

Font styles to use
Other font styles liked:
• Futura (not mandatory)

Colors

Designer to choose colors to be used in the design.

Requirements
Must have
• Modern, timeless design, not too bling bling
Nice to have
• Flat design
Should not have
• 3D, bling bling, many colours, etc

```html
<!DOCTYPE html>
<html lang="en">
<head>
<meta charset="utf-8">
<title>VEXTORANE ASP - 4M8 Control</title>
<link href="https://fonts.googleapis.com/css2?family=Source+Sans+3:wght@400;600&display=swap" rel="stylesheet">
<style>
:root{
  --page:#4b4b4b; --win:#1c1c1c; --title:#2e2e2e; --bar:#262626; --panel:#2a2a2a;
  --field:#1d1d1d; --btn:#4b4b4b; --tab:#3a3a3a; --text:#d8d8d8; --muted:#8c8c8c;
  --dim:#6f6f6f; --accent:#ff7d0a; --fader:#5f7d98; --track:#3a3a3a; --knob:#7c7c7c;
  --in:#5a7893; --out:#e2b306; --check:#6aa829; --line:#343434;
}
*{box-sizing:border-box;margin:0;padding:0}
html,body{width:1002px;height:1200px;overflow:hidden;background:var(--page)}
body{font-family:"Source Sans 3",sans-serif;color:var(--text)}
.stage{position:absolute;left:0;top:0;width:1504px;height:1802px;transform:scale(.6662);transform-origin:0 0}
.window{position:absolute;left:69px;width:1366px;height:768px;background:var(--win)}
.titlebar{position:absolute;left:0;top:0;width:100%;height:40px;background:var(--title);display:flex;align-items:center;justify-content:center;font-size:13px;letter-spacing:.3px;gap:8px}
.brand{position:absolute;left:16px;top:7px;display:flex;align-items:center;gap:5px;font-size:9px;color:var(--text)}
.brand i{width:26px;height:26px;background:#1f3a52;display:block}
.tabbar{position:absolute;left:0;top:40px;width:100%;height:55px;background:var(--bar)}
.tabs{position:absolute;left:16px;top:12px;display:flex;gap:4px}
.tab{width:74px;height:32px;background:var(--tab);font-size:12px;display:flex;align-items:center;justify-content:center;border-radius:2px}
.tab.wide{width:78px}
.tab.active{background:var(--accent);color:#fff;font-weight:600}
.device{position:absolute;left:1142px;top:12px;width:168px;height:32px;background:var(--field);font-size:13px;padding-left:8px;display:flex;align-items:center}
.chev{position:absolute;right:10px;top:50%;width:8px;height:5px;margin-top:-2px}
.gear{position:absolute;left:1329px;top:17px;width:22px;height:22px}
.panel{position:absolute;background:var(--panel)}
/* sidebar */
.lbl{position:absolute;left:16px;font-size:10px;letter-spacing:.3px;color:var(--muted)}
.btn{position:absolute;height:24px;width:78px;background:var(--btn);font-size:11px;display:flex;align-items:center;justify-content:center;border-radius:2px}
.field{position:absolute;left:16px;width:168px;height:32px;background:var(--field);font-size:12.5px;display:flex;align-items:center;padding-left:8px}
.field.ph{color:var(--dim)}
.sep{position:absolute;left:0;width:100%;height:2px;background:var(--win)}
.check{width:15px;height:15px;background:#f2f2f2;border-radius:2px;display:inline-block;flex:none}
.check.on{background:var(--check);position:relative}
.check.on::after{content:"";position:absolute;left:4px;top:1px;width:5px;height:9px;border:solid #fff;border-width:0 2px 2px 0;transform:rotate(45deg)}
/* channel groups */
.group{position:absolute;top:104px;width:214px;height:656px;background:var(--panel)}
.badge{position:absolute;left:-18px;top:0;width:18px;height:57px;display:flex;align-items:center;justify-content:center}
.badge span{transform:rotate(-90deg);font-size:10px;font-weight:600;color:#fff}
.badge.in{background:var(--in)} .badge.out{background:var(--out)}
.strip{position:absolute;top:0;width:107px;height:100%}
.strip+.strip{left:107px;border-left:1px solid var(--win)}
.scale{position:absolute;left:0;top:17px;width:38px;height:514px;display:flex;flex-direction:column;justify-content:space-between;align-items:flex-end}
.scale span{font-size:12px;line-height:14px;color:var(--dim)}
.ticks{position:absolute;left:43px;top:24px;width:9px;height:501px;background:repeating-linear-gradient(to bottom,#4e4e4e 0 1px,transparent 1px 5px)}
.fader{position:absolute;left:64px;top:16px;width:7px;height:508px;background:var(--track);border-radius:4px}
.fader .fill{position:absolute;left:0;right:0;bottom:0;top:calc(var(--k) - 16px);background:var(--fader);border-radius:0 0 4px 4px}
.fader .knob{position:absolute;left:-9px;top:calc(var(--k) - 28px);width:25px;height:25px;border-radius:50%;background:var(--knob);box-shadow:0 1px 2px rgba(0,0,0,.5)}
.fader .knob::after{content:"";position:absolute;left:0;right:0;top:12px;height:1px;background:#3a3a3a}
.meter{position:absolute;left:84px;top:16px;width:6px;height:508px;background:var(--track);border-radius:3px;overflow:hidden}
.meter i{position:absolute;left:0;right:0;bottom:0;top:calc(var(--m) - 16px);background:linear-gradient(to top,#19e58f 0%,#6fd64a 40%,#d9c51a 75%,#e8b500 100%);background-size:100% 508px;background-position:bottom}
.val,.sel{position:absolute;left:16px;width:74px;height:24px;background:var(--field);font-size:11.5px;display:flex;align-items:center;padding-left:6px}
.val{top:561px} .sel{top:591px}
.val em{font-style:normal;position:absolute;right:7px;color:var(--muted);font-size:10.5px}
.mute{position:absolute;left:16px;top:625px;display:flex;align-items:center;gap:6px;font-size:11px;color:var(--muted)}
.link{position:absolute;left:96px;top:535px;width:23px;height:23px;border-radius:50%;background:var(--fader);z-index:2}
/* eq */
.eqhead{position:absolute;left:0;top:0;width:100%;height:47px;font-size:10px;color:var(--muted);letter-spacing:.3px}
.eqhead span{position:absolute;top:18px}
.rows{position:absolute;left:0;top:47px;width:100%}
.row{height:55px;margin-top:4px;background:var(--panel);position:relative}
.rows{background:var(--win)}
.row>*{position:absolute;top:16px}
.cell{height:24px;background:var(--field);font-size:11.5px;display:flex;align-items:center;padding-left:5px}
.cell em{font-style:normal;position:absolute;right:7px;color:var(--muted);font-size:10.5px}
.graph{position:absolute;left:324px;top:105px;width:918px;height:587px;background:var(--panel)}
.fxbar{position:absolute;top:697px;height:48px;background:var(--panel);display:flex;align-items:center;font-size:12px;gap:8px;padding-left:16px}
.fxbar .cell{position:relative;height:24px}
</style>
</head>
<body>
<div class="stage">

<!-- Main mixer window -->
<section class="window" style="top:95px">
  <header class="titlebar">
    <div class="brand"><i></i>VEXTORANE</div>
    <span>VEXTORANE ASP - 4M8</span>
    <svg width="16" height="16" viewBox="0 0 16 16" fill="none" stroke="#cfcfcf" stroke-width="1.2"><path d="M3 13l1-4 7-7 3 3-7 7z M2 15h12"/></svg>
  </header>
  <nav class="tabbar">
    <div class="tabs">
      <div class="tab wide active">MAIN</div><div class="tab wide">X-OVER</div>
      <div class="tab">IN 1</div><div class="tab">IN 2</div><div class="tab">IN 3</div><div class="tab">IN 4</div>
      <div class="tab">OUT 1</div><div class="tab">OUT 2</div><div class="tab">OUT 3</div><div class="tab">OUT 4</div>
      <div class="tab">OUT 5</div><div class="tab">OUT 6</div><div class="tab">OUT 7</div><div class="tab">OUT 8</div>
    </div>
    <div class="device">Lumen<svg class="chev" viewBox="0 0 8 5"><path d="M0 0l4 4 4-4" fill="none" stroke="#888"/></svg></div>
    <svg class="gear" viewBox="0 0 24 24" fill="none" stroke="#9a9a9a" stroke-width="1.5"><circle cx="12" cy="12" r="3.5"/><path d="M12 2l2 3 3.5-1 .5 3.5 3.5 1-1.5 3.5 1.5 3-3.5 1-.5 3.5-3.5-1-2 3-2-3-3.5 1-.5-3.5-3.5-1 1.5-3-1.5-3.5 3.5-1 .5-3.5 3.5 1z"/></svg>
  </nav>

  <aside class="panel" style="left:8px;top:104px;width:200px;height:656px">
    <div class="lbl" style="top:17px">LOCAL PRESETS</div>
    <div class="btn" style="left:16px;top:38px">STORE</div><div class="btn" style="left:106px;top:38px">LOAD</div>
    <div class="sep" style="top:79px"></div>
    <div class="lbl" style="top:96px">UNIT PRESETS</div>
    <div class="field ph" style="top:117px">Enter Name</div>
    <div class="field" style="top:157px">- Select Preset -<svg class="chev" viewBox="0 0 8 5"><path d="M0 0l4 4 4-4" fill="none" stroke="#888"/></svg></div>
    <div class="btn" style="left:16px;top:205px">STORE</div><div class="btn" style="left:106px;top:205px">LOAD</div>
    <div class="sep" style="top:245px"></div>
    <div class="lbl" style="top:263px">LINK</div>
    <div class="field" style="top:284px">- Select Link -<svg class="chev" viewBox="0 0 8 5"><path d="M0 0l4 4 4-4" fill="none" stroke="#888"/></svg></div>
    <div class="sep" style="top:332px"></div>
    <div class="lbl" style="top:350px">UNIT NAME</div>
    <div class="field" style="top:371px">VEXTORANE ASP - 4M8</div>
    <div class="sep" style="top:419px"></div>
    <div class="lbl" style="top:437px">STATUS</div>
    <div style="position:absolute;left:16px;top:466px;width:10px;height:10px;border-radius:50%;background:#555"></div>
    <div style="position:absolute;left:36px;top:463px;font-size:12px">Disable</div>
    <div class="btn" style="left:106px;top:458px">DETAILS</div>
    <div class="sep" style="top:498px"></div>
    <div class="lbl" style="top:517px">VOLUME</div>
    <div style="position:absolute;left:121px;top:516px;display:flex;gap:8px;align-items:center;font-size:11px;color:var(--muted)">Mute All<span class="check"></span></div>
    <svg style="position:absolute;left:17px;top:546px" width="14" height="12" viewBox="0 0 14 12" fill="none" stroke="#888"><path d="M1 4h3l4-3v10L4 8H1z M10 4q2 2 0 4"/></svg>
    <div style="position:absolute;left:36px;top:546px;width:148px;height:12px;background:var(--field)"><div style="width:23px;height:100%;background:repeating-linear-gradient(to right,#e8b500 0 1px,transparent 1px 3px)"></div></div>
    <div class="sep" style="top:575px"></div>
    <div class="lbl" style="top:593px">TEMPERATURE</div>
    <div style="position:absolute;left:15px;top:606px;font-size:32px;color:#cfcfcf">32<sup style="font-size:18px">O</sup> C</div>
    <svg style="position:absolute;left:170px;top:613px" width="14" height="28" viewBox="0 0 14 28" fill="none" stroke="#e8b500" stroke-width="2"><path d="M4 18V4a3 3 0 016 0v14a5 5 0 11-6 0z"/><circle cx="7" cy="21" r="2" fill="#e8b500"/></svg>
  </aside>

  <!-- IN 1 / IN 2 -->
  <div class="group" style="left:234px">
    <div class="badge in"><span>IN</span></div>
    <div class="strip" style="--k:214px;--m:252px"><div class="scale"><span>+12</span><span>+6</span><span>0</span><span>-6</span><span>-12</span><span>-18</span><span>-24</span><span>-30</span><span>-36</span><span>-42</span><span>-48</span></div><div class="ticks"></div><div class="fader"><i class="fill"></i><b class="knob"></b></div><div class="meter"><i></i></div><div class="val">-12.2<em>dB</em></div><div class="sel">IN - 1<svg class="chev" viewBox="0 0 8 5"><path d="M0 0l4 4 4-4" fill="none" stroke="#888"/></svg></div><div class="mute"><span class="check"></span>Mute</div></div>
    <div class="strip" style="--k:279px;--m:150px"><div class="scale"><span>+12</span><span>+6</span><span>0</span><span>-6</span><span>-12</span><span>-18</span><span>-24</span><span>-30</span><span>-36</span><span>-42</span><span>-48</span></div><div class="ticks"></div><div class="fader"><i class="fill"></i><b class="knob"></b></div><div class="meter"><i></i></div><div class="val">-24.9<em>dB</em></div><div class="sel">IN - 2<svg class="chev" viewBox="0 0 8 5"><path d="M0 0l4 4 4-4" fill="none" stroke="#888"/></svg></div><div class="mute"><span class="check"></span>Mute</div></div>
    <svg class="link" viewBox="0 0 23 23" fill="none" stroke="#fff" stroke-width="1.6"><rect x="5" y="8.5" width="7" height="6" rx="3"/><rect x="11" y="8.5" width="7" height="6" rx="3"/></svg>
  </div>
  <!-- IN 3 / IN 4 -->
  <div class="group" style="left:457px;width:215px">
    <div class="strip" style="--k:409px;--m:422px"><div class="scale"><span>+12</span><span>+6</span><span>0</span><span>-6</span><span>-12</span><span>-18</span><span>-24</span><span>-30</span><span>-36</span><span>-42</span><span>-48</span></div><div class="ticks"></div><div class="fader"><i class="fill"></i><b class="knob"></b></div><div class="meter"><i></i></div><div class="val">-36.3<em>dB</em></div><div class="sel">IN - 3<svg class="chev" viewBox="0 0 8 5"><path d="M0 0l4 4 4-4" fill="none" stroke="#888"/></svg></div><div class="mute"><span class="check"></span>Mute</div></div>
    <div class="strip" style="--k:184px;--m:335px"><div class="scale"><span>+12</span><span>+6</span><span>0</span><span>-6</span><span>-12</span><span>-18</span><span>-24</span><span>-30</span><span>-36</span><span>-42</span><span>-48</span></div><div class="ticks"></div><div class="fader"><i class="fill"></i><b class="knob"></b></div><div class="meter"><i></i></div><div class="val">-12.8<em>dB</em></div><div class="sel">IN - 3<svg class="chev" viewBox="0 0 8 5"><path d="M0 0l4 4 4-4" fill="none" stroke="#888"/></svg></div><div class="mute"><span class="check"></span>Mute</div></div>
    <svg class="link" viewBox="0 0 23 23" fill="none" stroke="#fff" stroke-width="1.6"><rect x="5" y="8.5" width="7" height="6" rx="3"/><rect x="11" y="8.5" width="7" height="6" rx="3"/></svg>
  </div>
  <!-- OUT 1 / OUT 2 -->
  <div class="group" style="left:697px;width:215px">
    <div class="badge out"><span>OUT</span></div>
    <div class="strip" style="--k:214px;--m:449px"><div class="scale"><span>+12</span><span>+6</span><span>0</span><span>-6</span><span>-12</span><span>-18</span><span>-24</span><span>-30</span><span>-36</span><span>-42</span><span>-48</span></div><div class="ticks"></div><div class="fader"><i class="fill"></i><b class="knob"></b></div><div class="meter"><i></i></div><div class="val">-12.2<em>dB</em></div><div class="sel">OUT - 1<svg class="chev" viewBox="0 0 8 5"><path d="M0 0l4 4 4-4" fill="none" stroke="#888"/></svg></div><div class="mute"><span class="check"></span>Mute</div></div>
    <div class="strip" style="--k:279px;--m:299px"><div class="scale"><span>+12</span><span>+6</span><span>0</span><span>-6</span><span>-12</span><span>-18</span><span>-24</span><span>-30</span><span>-36</span><span>-42</span><span>-48</span></div><div class="ticks"></div><div class="fader"><i class="fill"></i><b class="knob"></b></div><div class="meter"><i></i></div><div class="val">-24.9<em>dB</em></div><div class="sel">OUT - 2<svg class="chev" viewBox="0 0 8 5"><path d="M0 0l4 4 4-4" fill="none" stroke="#888"/></svg></div><div class="mute"><span class="check"></span>Mute</div></div>
    <svg class="link" viewBox="0 0 23 23" fill="none" stroke="#fff" stroke-width="1.6"><rect x="5" y="8.5" width="7" height="6" rx="3"/><rect x="11" y="8.5" width="7" height="6" rx="3"/></svg>
  </div>
  <!-- OUT 3 / OUT 4 -->
  <div class="group" style="left:920px;width:215px">
    <div class="strip" style="--k:214px;--m:271px"><div class="scale"><span>+12</span><span>+6</span><span>0</span><span>-6</span><span>-12</span><span>-18</span><span>-24</span><span>-30</span><span>-36</span><span>-42</span><span>-48</span></div><div class="ticks"></div><div class="fader"><i class="fill"></i><b class="knob"></b></div><div class="meter"><i></i></div><div class="val">-12.2<em>dB</em></div><div class="sel">OUT - 3<svg class="chev" viewBox="0 0 8 5"><path d="M0 0l4 4 4-4" fill="none" stroke="#888"/></svg></div><div class="mute"><span class="check"></span>Mute</div></div>
    <div class="strip" style="--k:214px;--m:476px"><div class="scale"><span>+12</span><span>+6</span><span>0</span><span>-6</span><span>-12</span><span>-18</span><span>-24</span><span>-30</span><span>-36</span><span>-42</span><span>-48</span></div><div class="ticks"></div><div class="fader"><i class="fill"></i><b class="knob"></b></div><div class="meter"><i></i></div><div class="val">-12.2<em>dB</em></div><div class="sel">OUT - 4<svg class="chev" viewBox="0 0 8 5"><path d="M0 0l4 4 4-4" fill="none" stroke="#888"/></svg></div><div class="mute"><span class="check"></span>Mute</div></div>
    <svg class="link" viewBox="0 0 23 23" fill="none" stroke="#fff" stroke-width="1.6"><rect x="5" y="8.5" width="7" height="6" rx="3"/><rect x="11" y="8.5" width="7" height="6" rx="3"/></svg>
  </div>
  <!-- OUT 5 / OUT 6 -->
  <div class="group" style="left:1143px;width:215px">
    <div class="strip" style="--k:74px;--m:406px"><div class="scale"><span>+12</span><span>+6</span><span>0</span><span>-6</span><span>-12</span><span>-18</span><span>-24</span><span>-30</span><span>-36</span><span>-42</span><span>-48</span></div><div class="ticks"></div><div class="fader"><i class="fill"></i><b class="knob"></b></div><div class="meter"><i></i></div><div class="val">+6.0<em>dB</em></div><div class="sel">OUT - 5<svg class="chev" viewBox="0 0 8 5"><path d="M0 0l4 4 4-4" fill="none" stroke="#888"/></svg></div><div class="mute"><span class="check"></span>Mute</div></div>
    <div class="strip" style="--k:489px;--m:516px"><div class="scale"><span>+12</span><span>+6</span><span>0</span><span>-6</span><span>-12</span><span>-18</span><span>-24</span><span>-30</span><span>-36</span><span>-42</span><span>-48</span></div><div class="ticks"></div><div class="fader"><i class="fill"></i><b class="knob"></b></div><div class="meter"><i></i></div><div class="val">-48.7<em>dB</em></div><div class="sel">OUT - 6<svg class="chev" viewBox="0 0 8 5"><path d="M0 0l4 4 4-4" fill="none" stroke="#888"/></svg></div><div class="mute"><span class="check on"></span>Mute</div></div>
    <svg class="link" viewBox="0 0 23 23" fill="none" stroke="#fff" stroke-width="1.6"><rect x="5" y="8.5" width="7" height="6" rx="3"/><rect x="11" y="8.5" width="7" height="6" rx="3"/></svg>
  </div>
</section>

<!-- Input channel EQ window -->
<section class="window" style="top:940px">
  <header class="titlebar">
    <div class="brand"><i></i>VEXTORANE</div>
    <span>VEXTORANE ASP - 4M8</span>
    <svg width="16" height="16" viewBox="0 0 16 16" fill="none" stroke="#cfcfcf" stroke-width="1.2"><path d="M3 13l1-4 7-7 3 3-7 7z M2 15h12"/></svg>
  </header>
  <nav class="tabbar">
    <div class="tabs">
      <div class="tab wide">MAIN</div><div class="tab wide">X-OVER</div>
      <div class="tab active">IN 1</div><div class="tab">IN 2</div><div class="tab">IN 3</div><div class="tab">IN 4</div>
      <div class="tab">OUT 1</div><div class="tab">OUT 2</div><div class="tab">OUT 3</div><div class="tab">OUT 4</div>
      <div class="tab">OUT 5</div><div class="tab">OUT 6</div><div class="tab">OUT 7</div><div class="tab">OUT 8</div>
    </div>
    <div class="device">Lumen<svg class="chev" viewBox="0 0 8 5"><path d="M0 0l4 4 4-4" fill="none" stroke="#888"/></svg></div>
    <svg class="gear" viewBox="0 0 24 24" fill="none" stroke="#9a9a9a" stroke-width="1.5"><circle cx="12" cy="12" r="3.5"/><path d="M12 2l2 3 3.5-1 .5 3.5 3.5 1-1.5 3.5 1.5 3-3.5 1-.5 3.5-3.5-1-2 3-2-3-3.5 1-.5-3.5-3.5-1 1.5-3-1.5-3.5 3.5-1 .5-3.5 3.5 1z"/></svg>
  </nav>

  <div class="panel" style="left:8px;top:105px;width:308px;height:640px;background:var(--win)">
    <div class="eqhead" style="background:var(--panel)"><span style="left:42px">TYPE</span><span style="left:146px">FREQ</span><span style="left:220px">Q</span><span style="left:242px">GAIN</span></div>
    <div class="rows">
      <div class="row"><span class="check" style="left:16px;top:20px"></span><div class="cell" style="left:42px;width:99px">Band Pass<svg class="chev" viewBox="0 0 8 5"><path d="M0 0l4 4 4-4" fill="none" stroke="#888"/></svg></div><div class="cell" style="left:146px;width:60px">20<em>Hz</em></div><div class="cell" style="left:211px;width:26px">20</div><div class="cell" style="left:242px;width:50px">-12<em>dB</em></div></div>
      <div class="row"><span class="check" style="left:16px;top:20px"></span><div class="cell" style="left:42px;width:99px">Band Pass<svg class="chev" viewBox="0 0 8 5"><path d="M0 0l4 4 4-4" fill="none" stroke="#888"/></svg></div><div class="cell" style="left:146px;width:60px">20<em>Hz</em></div><div class="cell" style="left:211px;width:26px">20</div><div class="cell" style="left:242px;width:50px">-12<em>dB</em></div></div>
      <div class="row"><span class="check" style="left:16px;top:20px"></span><div class="cell" style="left:42px;width:99px">Band Pass<svg class="chev" viewBox="0 0 8 5"><path d="M0 0l4 4 4-4" fill="none" stroke="#888"/></svg></div><div class="cell" style="left:146px;width:60px">20<em>Hz</em></div><div class="cell" style="left:211px;width:26px">20</div><div class="cell" style="left:242px;width:50px">-12<em>dB</em></div></div>
      <div class="row"><span class="check" style="left:16px;top:20px"></span><div class="cell" style="left:42px;width:99px">Band Pass<svg class="chev" viewBox="0 0 8 5"><path d="M0 0l4 4 4-4" fill="none" stroke="#888"/></svg></div><div class="cell" style="left:146px;width:60px">20<em>Hz</em></div><div class="cell" style="left:211px;width:26px">20</div><div class="cell" style="left:242px;width:50px">-12<em>dB</em></div></div>
      <div class="row"><span class="check" style="left:16px;top:20px"></span><div class="cell" style="left:42px;width:99px">Band Pass<svg class="chev" viewBox="0 0 8 5"><path d="M0 0l4 4 4-4" fill="none" stroke="#888"/></svg></div><div class="cell" style="left:146px;width:60px">20<em>Hz</em></div><div class="cell" style="left:211px;width:26px">20</div><div class="cell" style="left:242px;width:50px">-12<em>dB</em></div></div>
      <div class="row"><span class="check" style="left:16px;top:20px"></span><div class="cell" style="left:42px;width:99px">Band Pass<svg class="chev" viewBox="0 0 8 5"><path d="M0 0l4 4 4-4" fill="none" stroke="#888"/></svg></div><div class="cell" style="left:146px;width:60px">20<em>Hz</em></div><div class="cell" style="left:211px;width:26px">20</div><div class="cell" style="left:242px;width:50px">-12<em>dB</em></div></div>
      <div class="row"><span class="check" style="left:16px;top:20px"></span><div class="cell" style="left:42px;width:99px">Band Pass<svg class="chev" viewBox="0 0 8 5"><path d="M0 0l4 4 4-4" fill="none" stroke="#888"/></svg></div><div class="cell" style="left:146px;width:60px">20<em>Hz</em></div><div class="cell" style="left:211px;width:26px">20</div><div class="cell" style="left:242px;width:50px">-12<em>dB</em></div></div>
      <div class="row"><span class="check" style="left:16px;top:20px"></span><div class="cell" style="left:42px;width:99px">Band Pass<svg class="chev" viewBox="0 0 8 5"><path d="M0 0l4 4 4-4" fill="none" stroke="#888"/></svg></div><div class="cell" style="left:146px;width:60px">20<em>Hz</em></div><div class="cell" style="left:211px;width:26px">20</div><div class="cell" style="left:242px;width:50px">-12<em>dB</em></div></div>
      <div class="row"><span class="check" style="left:16px;top:20px"></span><div class="cell" style="left:42px;width:99px">Band Pass<svg class="chev" viewBox="0 0 8 5"><path d="M0 0l4 4 4-4" fill="none" stroke="#888"/></svg></div><div class="cell" style="left:146px;width:60px">20<em>Hz</em></div><div class="cell" style="left:211px;width:26px">20</div><div class="cell" style="left:242px;width:50px">-12<em>dB</em></div></div>
      <div class="row"><span class="check" style="left:16px;top:20px"></span><div class="cell" style="left:42px;width:99px">Band Pass<svg class="chev" viewBox="0 0 8 5"><path d="M0 0l4 4 4-4" fill="none" stroke="#888"/></svg></div><div class="cell" style="left:146px;width:60px">20<em>Hz</em></div><div class="cell" style="left:211px;width:26px">20</div><div class="cell" style="left:242px;width:50px">-12<em>dB</em></div></div>
    </div>
  </div>

  <svg class="graph" viewBox="0 0 918 587">
    <g stroke="#353535" stroke-width="1">
      <path d="M22 0V587M73 0V587M109 0V587M137 0V587M160 0V587M179 0V587M196 0V587M211 0V587M311 0V587M362 0V587M398 0V587M426 0V587M449 0V587M468 0V587M485 0V587M500 0V587M600 0V587M651 0V587M687 0V587M715 0V587M738 0V587M757 0V587M774 0V587M789 0V587M889 0V587"/>
      <path d="M0 293H918" stroke="#3e3e3e"/>
    </g>
    <defs><linearGradient id="bell" x1="0" y1="0" x2="0" y2="1"><stop offset="0" stop-color="#2fa873" stop-opacity=".22"/><stop offset="1" stop-color="#2fa873" stop-opacity=".04"/></linearGradient></defs>
    <path d="M22 296 C180 272 290 172 393 172 C496 172 620 272 889 295 L889 293 L22 293Z" fill="url(#bell)"/>
    <path d="M22 296 C180 272 290 172 393 172 C496 172 620 272 889 295" fill="none" stroke="#2fa873" stroke-width="1.3"/>
    <g font-family="Source Sans 3, sans-serif" font-size="8" fill="#fff" text-anchor="middle">
      <circle cx="67" cy="293" r="7" fill="#d9534f"/><text x="67" y="296">1</text>
      <circle cx="164" cy="293" r="7" fill="#7aa035"/><text x="164" y="296">2</text>
      <circle cx="198" cy="293" r="7" fill="#d99a20"/><text x="198" y="296">3</text>
      <circle cx="245" cy="293" r="7" fill="#cf4fcf"/><text x="245" y="296">4</text>
      <circle cx="349" cy="293" r="7" fill="#3f8fd8"/><text x="349" y="296">5</text>
      <circle cx="393" cy="172" r="7" fill="#2fa873"/><text x="393" y="175">6</text>
      <circle cx="447" cy="293" r="7" fill="#a89a3c"/><text x="447" y="296">7</text>
      <circle cx="527" cy="293" r="7" fill="#d43b6a"/><text x="527" y="296">8</text>
      <circle cx="658" cy="293" r="7" fill="#9a3b40"/><text x="658" y="296">9</text>
      <circle cx="748" cy="293" r="7" fill="#2a4fd0"/><text x="748" y="296">10</text>
    </g>
  </svg>

  <div class="fxbar" style="left:324px;width:230px"><span class="check"></span>HPF<div class="cell" style="width:150px;margin-left:4px">Linkwitz-Riley 24dB<svg class="chev" viewBox="0 0 8 5"><path d="M0 0l4 4 4-4" fill="none" stroke="#888"/></svg></div></div>
  <div class="fxbar" style="left:559px;width:229px"><span class="check"></span>LPF<div class="cell" style="width:150px;margin-left:4px">Linkwitz-Riley 24dB<svg class="chev" viewBox="0 0 8 5"><path d="M0 0l4 4 4-4" fill="none" stroke="#888"/></svg></div></div>
  <div class="fxbar" style="left:804px;width:130px">Delay<div class="cell" style="width:60px">0<em>Ms</em></div></div>
  <div class="fxbar" style="left:939px;width:137px">Limiter<div class="cell" style="width:60px">0<em>dBu</em></div></div>
  <div class="fxbar" style="left:1081px;width:161px">Compressor<div class="cell" style="width:60px">0<em>dB/s</em></div></div>

  <div class="panel" style="left:1252px;top:105px;width:106px;height:640px">
    <div class="lbl" style="left:15px;top:16px">GAIN</div>
    <div class="scale" style="top:46px;width:48px"><span>+12</span><span>+6</span><span>0</span><span>-6</span><span>-12</span><span>-18</span><span>-24</span><span>-30</span><span>-36</span><span>-42</span><span>-48</span></div>
    <div class="ticks" style="left:52px;top:53px;width:8px"></div>
    <div class="fader" style="left:64px;top:45px;--k:223px"><i class="fill" style="top:calc(var(--k) - 16px)"></i><b class="knob"></b></div>
    <div class="meter" style="top:45px;left:83px"><i style="top:65px;background:linear-gradient(to top,#19e58f 0%,#8bd43c 45%,#e3c21a 70%,#f08a10 88%,#e8421a 100%)"></i></div>
    <div class="val" style="top:573px;width:75px">-12.0<em>dB</em></div>
    <div class="mute" style="top:608px"><span class="check"></span>Mute</div>
  </div>
</section>

</div>
</body>
</html>
```